jewelry,purses,pj's,and retro bathing caps

I need a business card to hand out to people because i wear my jewelry and also to put in box with purchases. I want a card with maybe me as a redhead covered in jewelry carrying an overflowing shopping bag.
Target Market(s)
my tradlo customers and people on the street who compliment me about my jewelry
Industry/Entity Type
Shopping
Contact Information for Business Card
glimmerboutique4719
This is my Tradlo Store
we guarantee happiness or money back
Font styles to use
Serif
Requirements
Must have
- pix of jewelry on a mannequin
the fact that I am a "crest lister"

```html
<!DOCTYPE html>
<html lang="en">
<head>
<meta charset="utf-8">
<title>Jewelry &amp; Accessories – Business Card</title>
<link rel="stylesheet" href="https://fonts.googleapis.com/css2?family=Questrial&family=Poppins:wght@600&display=swap">
<style>
  :root {
    --backdrop: #3b3c41;
    --card-white: #ffffff;
    --brand-purple: #b452ef;
    --name-purple: #a54fe8;
    --accent-red: #e0285a;
    --text-grey: #5e5e63;
    --figure-pink: #e23d6a;
    --figure-skin: #f2c7a0;
  }
  * { margin: 0; padding: 0; box-sizing: border-box; }
  html, body {
    width: 1200px;
    height: 1000px;
    overflow: hidden;
    background: var(--backdrop);
  }
  .business-card {
    position: absolute;
    left: 160px;
    top: 240px;
    width: 880px;
    height: 520px;
    border-radius: 44px;
    overflow: hidden;
    background: var(--card-white);
    font-family: "Questrial", sans-serif;
  }
  .card-shapes {
    position: absolute;
    inset: 0;
  }
  .shop-figure {
    position: absolute;
    left: 590px;
    top: 22px;
    width: 230px;
    height: 230px;
    border-radius: 50%;
    background: radial-gradient(circle at 50% 45%, var(--figure-pink) 0%, var(--figure-skin) 45%, rgba(180, 82, 239, 0) 72%);
  }
  .brand-title {
    position: absolute;
    left: 150px;
    top: 150px;
    color: #fff;
    font-size: 50px;
    letter-spacing: 0.5px;
  }
  .brand-tagline {
    position: absolute;
    left: 150px;
    top: 216px;
    color: #fff;
    font-size: 24px;
    letter-spacing: 0.4px;
  }
  .contact-block {
    position: absolute;
    right: 250px;
    top: 328px;
    text-align: right;
  }
  .owner-name {
    font-family: "Poppins", sans-serif;
    font-weight: 600;
    font-size: 34px;
    color: var(--name-purple);
    line-height: 46px;
  }
  .contact-line {
    font-size: 28px;
    color: var(--text-grey);
    line-height: 40px;
    letter-spacing: 1px;
  }
  .contact-icons {
    position: absolute;
    left: 646px;
    top: 378px;
  }
  .store-mark {
    position: absolute;
    left: 650px;
    top: 456px;
    font-family: "Poppins", sans-serif;
    font-weight: 600;
    font-size: 30px;
    color: var(--text-grey);
  }
</style>
</head>
<body>
  <main class="business-card">
    <svg class="card-shapes" width="880" height="520" viewBox="0 0 880 520">
      <path d="M0 0 H880 V300 L0 262 Z" fill="var(--brand-purple)"/>
      <line x1="0" y1="264" x2="880" y2="302" stroke="var(--accent-red)" stroke-width="5"/>
    </svg>

    <div class="shop-figure" role="img" aria-label="Illustration of a woman in a pink dress carrying colourful shopping bags"></div>

    <h1 class="brand-title">Jewelry &amp; Accessories</h1>
    <p class="brand-tagline">we guarantee happiness or money back</p>

    <section class="contact-block">
      <p class="owner-name">Your Name Here</p>
      <p class="contact-line">1234567910</p>
      <p class="contact-line">youremail@here.com</p>
      <p class="contact-line">glimmerboutique4719</p>
    </section>

    <svg class="contact-icons" width="40" height="80" viewBox="0 0 40 80" aria-hidden="true">
      <g class="icon-phone">
        <circle cx="18" cy="18" r="15" fill="var(--accent-red)"/>
        <rect x="12" y="9" width="12" height="18" rx="2" fill="none" stroke="#fff" stroke-width="2"/>
        <line x1="16" y1="24" x2="20" y2="24" stroke="#fff" stroke-width="2"/>
      </g>
      <g class="icon-mail">
        <circle cx="18" cy="58" r="15" fill="var(--accent-red)"/>
        <rect x="10" y="52" width="16" height="12" fill="none" stroke="#fff" stroke-width="2"/>
        <polyline points="10,52 18,59 26,52" fill="none" stroke="#fff" stroke-width="2"/>
      </g>
    </svg>

    <p class="store-mark">tradlo</p>
  </main>
</body>
</html>
```